2019 CD Cover Design - Drifting Past Noon

Please Use Uploaded Photo. Feel free to crop and otherwise edit the photo to enrich the design. Title is "Drifting Past Noon" and should be relative prominent in the cover. Artist names are "Marcus Pellham and Rosalind Quaye" and should also be printed on the cover. Please ensure compliance with DiscHarbor Published Requirements, ie CMYK, 300dpi, etc. Planning on giving winner the Back Cover and Inside designs.

Target Market(s)

The album is a set of cover love songs, all duets, many are contemporary country, ie in the style of Copper Wagonwheel, Greta Voss, Harlow Junction. Feel free to innovate!

Industry/Entity Type

Music Download

Colors

Designer to choose colors to be used in the design.

Requirements
Nice to have
• Optional - Third Line of Text - “Contemporary Country Duets”
Should not have
• Please do NOT cut out and completely replace the grassy field background. The CD liner notes will discuss the photo, which is a renowned national park in our hometown.

```html
<!DOCTYPE html>
<html lang="en">
<head>
<meta charset="utf-8">
<title>Drifting Past Noon — Album Cover</title>
<link rel="stylesheet" href="https://fonts.googleapis.com/css2?family=Oswald:wght@500&family=Mrs+Saint+Delafield&display=swap">
<style>
  :root {
    --paper: #ffffff;
    --field-gold: #8a7a3a;
    --field-dark: #3a3320;
    --shade: #141312;
    --title: #ffffff;
    --band: rgba(225, 225, 225, 0.85);
    --band-ink: #1a1a1a;
  }
  html, body {
    margin: 0;
    width: 1200px;
    height: 1200px;
    overflow: hidden;
    background: var(--paper);
  }
  .cover {
    position: relative;
    width: 1200px;
    height: 1200px;
    background: var(--paper);
  }
  .cover__photo {
    position: absolute;
    left: 0;
    top: 40px;
    width: 1200px;
    height: 1116px;
    background:
      radial-gradient(ellipse 40% 35% at 38% 35%, rgba(200,190,175,0.55), transparent 70%),
      radial-gradient(ellipse 35% 40% at 66% 52%, rgba(215,180,130,0.55), transparent 70%),
      linear-gradient(180deg, var(--field-dark) 0%, var(--field-gold) 30%, #6d6a3c 55%, var(--shade) 100%);
  }
  .cover__vignette {
    position: absolute;
    left: 0;
    top: 40px;
    width: 1200px;
    height: 1116px;
    background: linear-gradient(180deg, transparent 55%, rgba(10,10,10,0.75) 100%);
  }
  .cover__flares {
    position: absolute;
    left: 0;
    top: 40px;
  }
  .cover__title {
    position: absolute;
    left: 0;
    width: 1200px;
    top: 800px;
    margin: 0;
    text-align: center;
    font-family: "Mrs Saint Delafield", cursive;
    font-weight: 400;
    font-size: 190px;
    line-height: 1;
    color: var(--title);
    white-space: nowrap;
  }
  .cover__artists {
    position: absolute;
    left: 215px;
    top: 1046px;
    width: 765px;
    height: 38px;
    background: linear-gradient(90deg, transparent 0%, var(--band) 8%, var(--band) 85%, transparent 100%);
    display: flex;
    align-items: center;
    justify-content: center;
    margin: 0;
    font-family: "Oswald", sans-serif;
    font-weight: 500;
    font-size: 31px;
    letter-spacing: 1px;
    text-transform: uppercase;
    color: var(--band-ink);
  }
</style>
</head>
<body>
  <main class="cover">
    <div class="cover__photo" role="img" aria-label="Photo of the two duet artists kneeling in a sunlit grassy field in a national park"></div>
    <div class="cover__vignette"></div>
    <svg class="cover__flares" width="1200" height="1116" viewBox="0 0 1200 1116" aria-hidden="true">
      <circle cx="317" cy="783" r="120" fill="#c9904a" opacity="0.3"/>
      <circle cx="350" cy="770" r="68" fill="#d89e55" opacity="0.3"/>
      <circle cx="300" cy="793" r="33" fill="#d89e55" opacity="0.3"/>
      <circle cx="157" cy="873" r="50" fill="#4fa86a" opacity="0.35"/>
      <circle cx="838" cy="491" r="33" fill="#f0b070" opacity="0.45"/>
      <circle cx="1010" cy="392" r="48" fill="#b7d0c0" opacity="0.15"/>
      <circle cx="460" cy="702" r="5" fill="#c8ffe8" opacity="0.9"/>
      <circle cx="686" cy="575" r="4" fill="#e8ffd8" opacity="0.9"/>
    </svg>
    <h1 class="cover__title">Drifting Past Noon</h1>
    <p class="cover__artists">Marcus Pellham and Rosalind Quaye</p>
  </main>
</body>
</html>
```